Bright Reed Acupuncture Studio Website Design

We are working with Bright Reed Acunpuncture Studio. They are a local Chinese medicine and acupuncture studio and in need of a new website design.

Some sites to use for inspiration:

https://marblecoveacupuncture.example
https://steadfernacupuncture.example
https://quietharborclinic.example
https://emberdawnacupuncture.example
https://cedarbrookclinic.example

Thank you for taking the time to consider designing a website for us. We are web developers based in Stockton, CA, USA. Most of our projects go through the same process. Understanding this process may help you win a project with us. We custom-code all of our websites in-house. We don’t have any requirements as to what tools you use for your design, but we prefer Figma files. For any design that we label as four-stars, we send it to the client for review. The client picks the final design they want us to use. Once we complete this process, we will continue to show additional clients all the four-star sites and purchase them later. Your designs will have multiple chances to sell. For better chances of success, we ask that you follow these guidelines.

IMAGES:
If you use any images or icons in the design, we ask that you have a link to the asset so we can purchase the image/icon. Most of the designs we submit do not have the customer’s images on them unless they have some great images. Be creative; show us the feeling you are trying to portray with your image choices. Use any royalty-free site you choose. We subscribe to Adobe and mainly use their images, but we can purchase images outside of Adobe.

PLEASE NOTE: we will not submit designs to clients with watermarks on the images.

FONTS:
We ask that you identify the fonts used in the design. This can be done in a message if you want. We typically use Google Fonts and Adobe Fonts.

CONTENT:
We're always open to different content and ideas. We often submit designs with stock images so the client can see our vision. We typically take pictures after the website launch to use their images with our vision. Lorem Ipsum is fine for paragraphs, but we ask that you write the headers in correct English. We want to be able to show the vision and identify the sections of the website.

INSPIRATION:
We typically add a couple of links in the brief of websites we like to help you get started in your design.

REVISIONS:
We do not often ask for revisions of the designs unless we see something in the design that may not appeal to the client. If there are slight changes that we want to make, we do that in the development process.

FEEDBACK:
We rarely give feedback on designs during the design process. We are working on many website projects and do not have the time to provide feedback. We usually respond if your request is well thought out and asks specific questions, but a note asking “feedback, please” usually goes unanswered.

```html
<!DOCTYPE html>
<html lang="en">
<head>
<meta charset="UTF-8">
<title>Bright Reed Acupuncture Studio</title>
<link rel="stylesheet" href="https://fonts.googleapis.com/css2?family=Nunito+Sans:wght@300;400;700;800&family=Open+Sans:ital,wght@0,400;0,600;1,400&display=swap">
<style>
:root{
  --coral:#e0625a;
  --coral-soft:#e8776f;
  --ink:#1f2530;
  --text:#3a3d44;
  --muted:#5b5f66;
  --blush:#fdeeee;
  --white:#ffffff;
  --line:#e9c3c0;
}
*{margin:0;padding:0;box-sizing:border-box}
html,body{width:1200px;height:4185px;overflow:hidden;background:var(--white)}
body{font-family:"Open Sans",sans-serif;color:var(--text)}
.page{position:relative;width:1200px;height:4185px;overflow:hidden}
.abs{position:absolute}
.heading-font{font-family:"Nunito Sans",sans-serif}
.btn{position:absolute;display:flex;align-items:center;justify-content:center;background:var(--coral);color:var(--white);font-family:"Nunito Sans",sans-serif;font-weight:800;border-radius:30px;font-size:15px;text-decoration:none}

/* header */
.site-nav a{position:absolute;top:60px;font-size:16px;color:var(--text);text-decoration:none}
.site-nav a.active{color:var(--coral)}
.brand{position:absolute;display:flex;align-items:center;gap:12px;font-family:"Nunito Sans",sans-serif;font-weight:800;color:var(--ink)}
.brand .mark{width:38px;height:38px;border-radius:50%;background:var(--coral);flex:none}
.brand .name{font-size:26px;line-height:1.05}

/* hero */
.hero-photo{position:absolute;left:0;top:0;width:1200px;height:690px;background:linear-gradient(100deg,#dfe6ea 0%,#d6dfe3 35%,#e9cdbd 60%,#d9a98f 80%,#c98d74 100%)}
.hero-text{position:absolute;left:107px;top:201px;border-left:3px solid var(--ink);padding-left:12px}
.hero-text .light{font-family:"Nunito Sans",sans-serif;font-weight:300;font-size:40px;color:var(--ink);line-height:1.1}
.hero-text .bold{font-family:"Nunito Sans",sans-serif;font-weight:800;font-size:44px;color:var(--ink);line-height:1.3}
.hero-copy{position:absolute;left:120px;top:328px;width:400px;font-size:15px;line-height:26px;color:var(--ink)}

/* section titles */
.title-bar{position:absolute;height:3px;width:68px;background:var(--ink)}
.section-title{position:absolute;left:0;width:1200px;text-align:center;font-family:"Nunito Sans",sans-serif}
.section-title .accent{display:block;font-weight:300;color:var(--coral);font-size:44px;line-height:1.15}
.section-title .main{display:block;font-weight:800;color:var(--ink);font-size:44px;line-height:1.15}

/* about */
.about-photo{position:absolute;left:203px;top:768px;width:406px;height:406px;border-radius:50%;background:radial-gradient(circle at 40% 40%,#f4eee9,#e3d3c8 60%,#c8ada0)}
.about-head{position:absolute;left:658px;top:770px;border-left:3px solid var(--ink);padding-left:14px;font-family:"Nunito Sans",sans-serif}
.about-head .accent{font-weight:300;color:var(--coral);font-size:44px;line-height:1.1}
.about-head .main{font-weight:800;color:var(--ink);font-size:44px;line-height:1.2}
.about-copy{position:absolute;left:674px;top:893px;width:420px;font-size:15px;line-height:30px;color:var(--muted)}

/* services */
.services{position:absolute;left:0;top:1340px;width:1200px;height:638px;background:var(--blush)}
.service-card{position:absolute;top:1572px;width:239px;height:287px}
.service-label{position:absolute;top:1827px;height:60px;border-left:3px solid var(--ink);padding:40px 0 0 8px;font-family:"Nunito Sans",sans-serif;font-weight:800;font-size:16px;color:var(--ink)}
.service-card.active{background:var(--coral-soft);color:var(--white);padding:22px 22px 0 42px}
.service-card.active h3{font-family:"Nunito Sans",sans-serif;font-weight:800;font-size:16px;border-left:3px solid var(--white);margin-left:-20px;padding-left:17px;line-height:18px}
.service-card.active p{font-size:14.5px;line-height:24px;margin-top:22px}

/* why */
.why-item{position:absolute;width:400px}
.why-icon{position:absolute;width:106px;height:106px;border-radius:50%;background:var(--ink);display:flex;align-items:center;justify-content:center}
.why-icon .ring{width:80px;height:80px;border-radius:50%;border:2px solid var(--coral);display:flex;align-items:center;justify-content:center}
.why-item h3{position:absolute;font-family:"Nunito Sans",sans-serif;font-weight:800;font-size:21px;color:var(--ink);white-space:nowrap}
.why-item p{position:absolute;font-size:14.5px;line-height:26px;color:var(--muted);width:300px}

/* testimonials */
.testimonials{position:absolute;left:0;top:2764px;width:1200px;height:560px;background:radial-gradient(ellipse at 30% 30%,#eef0ea 0%,#f3f3f2 40%,#ececec 100%)}
.client-photo{position:absolute;left:181px;top:2961px;width:246px;height:246px;border-radius:50%;border:5px solid var(--white);background:radial-gradient(circle at 50% 40%,#c9a28a,#8a5a45 70%,#5b3a2e);box-shadow:0 2px 8px rgba(0,0,0,.12)}
.quote{position:absolute;left:474px;top:3061px;width:540px;font-style:italic;font-size:14.5px;line-height:24.5px;color:var(--muted)}
.dot{position:absolute;top:3194px;width:14px;height:14px;border-radius:50%;border:1.5px solid var(--muted)}
.dot.on{background:var(--coral);border-color:var(--coral)}

/* connect */
.connect-title{position:absolute;left:120px;top:3445px;font-family:"Nunito Sans",sans-serif;font-size:44px}
.connect-title .accent{font-weight:300;color:var(--coral)}
.connect-title .main{font-weight:800;color:var(--ink)}

/* footer */
.footer-nav a{position:absolute;top:3946px;font-size:18px;color:var(--white);text-decoration:none;transform:translateX(-50%)}
.social{position:absolute;top:4018px;width:42px;height:42px;border-radius:50%;border:2px solid var(--white)}
.copyright{position:absolute;left:0;top:4111px;width:1200px;text-align:center;color:var(--white);font-size:17px}
</style>
</head>
<body>
<div class="page">

  <!-- Hero -->
  <div class="hero-photo" role="img" aria-label="Photo of a smiling woman relaxing during an acupuncture treatment with fine needles"></div>
  <svg class="abs" style="left:0;top:0" width="1200" height="700" viewBox="0 0 1200 700" aria-hidden="true">
    <path d="M0 516 Q600 800 1200 516 L1200 700 L0 700 Z" fill="var(--coral)"/>
    <path d="M0 532 Q600 770 1200 522 L1200 700 L0 700 Z" fill="var(--white)"/>
  </svg>

  <nav class="site-nav">
    <a class="active" style="left:109px">Home</a>
    <a style="left:211px">About Us</a>
    <a style="left:338px">Services</a>
    <a style="left:793px">Schedule</a>
    <a style="left:918px">FAQ</a>
    <a style="left:1007px">Contact Us</a>
  </nav>
  <div class="brand" style="left:482px;top:36px">
    <span class="mark"></span>
    <span class="name">Bright Reed<br>Acupuncture Studio</span>
  </div>

  <div class="hero-text">
    <div class="light">Restoring Balance.</div>
    <div class="bold">Enhancing Wellness.</div>
  </div>
  <p class="hero-copy">Traditional Chinese Medicine &amp; Acupuncture in [Your City Name] — Rooted in Healing, Guided by Experience.</p>
  <a class="btn" style="left:120px;top:421px;width:223px;height:50px">Book an Appointment</a>

  <!-- About -->
  <div class="about-photo" role="img" aria-label="Photo of a practitioner placing acupuncture needles on a relaxed client"></div>
  <div class="about-head">
    <div class="accent">Your Healing</div>
    <div class="main">Journey Begins Here</div>
  </div>
  <p class="about-copy">At Bright Reed Acupuncture Studio, we specialize in holistic health rooted in the ancient traditions of Chinese medicine. Our mission is simple: to help you live pain-free, balanced, and vibrant. Whether you're seeking relief from chronic pain, stress, digestive issues, or simply looking to maintain wellness, we provide gentle, effective, and personalized care.</p>
  <a class="btn" style="left:676px;top:1127px;width:139px;height:52px">Learn More</a>

  <!-- Services -->
  <div class="services"></div>
  <div class="title-bar" style="left:567px;top:1415px"></div>
  <h2 class="section-title" style="top:1426px"><span class="accent">Our Services</span><span class="main">Traditional Chinese Medicine treatments</span></h2>

  <div class="service-card" style="left:109px;background:linear-gradient(160deg,#f1e6e1,#e2c6b8)" role="img" aria-label="Photo of acupuncture needles placed on a woman's face"></div>
  <div class="service-card active" style="left:357px">
    <h3>Cupping Therapy</h3>
    <p>Sed ut perspiciatis unde omnis iste natus error sit voluptatem accusantium doloremque laudantium, totam rem aperiam, eaque ipsa quae ab illo inventore veritatis et</p>
  </div>
  <div class="service-card" style="left:604px;background:linear-gradient(160deg,#4a4536,#6b6a45 50%,#3a352b)" role="img" aria-label="Photo of dried herbs being ground in a mortar"></div>
  <div class="service-card" style="left:853px;background:linear-gradient(160deg,#efe4dc,#d9b9a6)" role="img" aria-label="Photo of a gua sha stone massage on a woman's face"></div>

  <div class="service-label" style="left:127px">Acupuncture Therapy</div>
  <div class="service-label" style="left:621px">Herbal Medicine</div>
  <div class="service-label" style="left:869px">Gua Sha &amp; Tuina</div>

  <!-- Why choose us -->
  <div class="title-bar" style="left:567px;top:2083px"></div>
  <h2 class="section-title" style="top:2094px"><span class="accent">Why Choose Us</span><span class="main">The Bright Reed Difference</span></h2>

  <svg class="abs" style="left:140px;top:2246px" width="930" height="410" aria-hidden="true">
    <defs>
      <linearGradient id="hfade" x1="0" x2="1"><stop offset="0" stop-color="var(--coral)" stop-opacity="0"/><stop offset=".5" stop-color="var(--coral)" stop-opacity=".7"/><stop offset="1" stop-color="var(--coral)" stop-opacity="0"/></linearGradient>
      <linearGradient id="vfade" x1="0" y1="0" x2="0" y2="1"><stop offset="0" stop-color="#d8d8d8" stop-opacity="0"/><stop offset=".5" stop-color="#d8d8d8"/><stop offset="1" stop-color="#d8d8d8" stop-opacity="0"/></linearGradient>
    </defs>
    <rect x="461" y="0" width="1.5" height="410" fill="url(#vfade)"/>
    <rect x="0" y="197" width="930" height="1.5" fill="url(#hfade)"/>
  </svg>

  <div class="why-icon" style="left:127px;top:2277px"><div class="ring"><svg width="40" height="40" viewBox="0 0 40 40" fill="none" stroke="#fff" stroke-width="1.6"><circle cx="20" cy="13" r="6"/><path d="M9 32c2-7 20-7 22 0"/></svg></div></div>
  <div class="why-item"><h3 style="left:260px;top:2281px">Personalized Care Plans</h3><p style="left:259px;top:2322px;width:300px">Every treatment is tailored to your unique constitution and needs.</p></div>

  <div class="why-icon" style="left:639px;top:2277px"><div class="ring"><svg width="40" height="40" viewBox="0 0 40 40" fill="none" stroke="#fff" stroke-width="1.6"><path d="M7 20h26c0 8-6 12-13 12S7 28 7 20z"/><path d="M20 20V8M20 12l-5-4M20 12l5-4"/></svg></div></div>
  <div class="why-item"><h3 style="left:771px;top:2281px">Rooted in Tradition</h3><p style="left:771px;top:2322px;width:300px">Evidence-backed care grounded in ancient practices.</p></div>

  <div class="why-icon" style="left:127px;top:2494px"><div class="ring"><svg width="40" height="40" viewBox="0 0 40 40" fill="none" stroke="#fff" stroke-width="1.6"><circle cx="20" cy="20" r="12"/><circle cx="20" cy="20" r="5"/></svg></div></div>
  <div class="why-item"><h3 style="left:260px;top:2498px">Tranquil Healing Space</h3><p style="left:259px;top:2539px;width:280px">Relax and rejuvenate in our calming, thoughtfully designed clinic.</p></div>

  <div class="why-icon" style="left:639px;top:2494px"><div class="ring"><svg width="40" height="40" viewBox="0 0 40 40" fill="none" stroke="#fff" stroke-width="1.6"><path d="M20 8c5 6 5 14 0 20c-5-6-5-14 0-20z"/><path d="M8 22c6 0 10 4 12 8c-6 0-10-3-12-8zM32 22c-6 0-10 4-12 8c6 0 10-3 12-8z"/></svg></div></div>
  <div class="why-item"><h3 style="left:768px;top:2498px">Holistic Support</h3><p style="left:770px;top:2539px;width:300px">Beyond symptom relief, we guide you in full-body wellness and self-care.</p></div>

  <!-- Testimonials -->
  <div class="testimonials" role="img" aria-label="Soft pale marble texture background"></div>
  <div class="title-bar" style="left:567px;top:2846px"></div>
  <h2 class="abs heading-font" style="left:0;top:2860px;width:1200px;text-align:center;font-size:44px"><span style="font-weight:300;color:var(--coral)">Our</span>&nbsp; <span style="font-weight:800;color:var(--ink)">Testimonials</span></h2>
  <div class="client-photo" role="img" aria-label="Portrait photo of a smiling client"></div>
  <svg class="abs" style="left:474px;top:2973px" width="146" height="24" viewBox="0 0 146 24" aria-label="Five star rating">
    <g fill="var(--coral)">
      <path id="star" d="M11 1l3 7h7l-6 4.5 2.3 7.5L11 15.5 4.7 20 7 12.5 1 8h7z"/>
      <use href="#star" x="31"/><use href="#star" x="62"/><use href="#star" x="93"/><use href="#star" x="124"/>
    </g>
  </svg>
  <div class="abs" style="left:473px;top:3005px;font-size:23px;color:var(--ink)">Marissa K.</div>
  <p class="quote">Sed ut perspiciatis unde omnis iste natus error sit voluptatem accusantium doloremque laudantium, totam rem aperiam, eaque ipsa quae ab illo inventore veritatis et quasi architecto beatae vitae dicta sunt explicabo. Nemo enim ipsam voluptatem quia voluptas sit aspernatur aut odit aut fugit, sed quia consequuntur magni dolores eos qui ratione voluptatem sequi nesciunt.</p>
  <span class="dot on" style="left:473px"></span>
  <span class="dot" style="left:500px"></span>
  <span class="dot" style="left:521px"></span>
  <span class="dot" style="left:542px"></span>

  <!-- Connect -->
  <div class="title-bar" style="left:120px;top:3430px"></div>
  <h2 class="connect-title"><span class="accent">Let’s</span> <span class="main">Connect</span></h2>
  <p class="abs" style="left:122px;top:3514px;width:600px;font-size:15px;line-height:26px;color:var(--muted)">Lorem ipsum dolor sit amet, consectetur adipiscing elit, sed do eiusmod tempor incididunt ut labore et dolore magna aliqua.</p>
  <a class="btn" style="left:831px;top:3467px;width:244px;height:57px;font-size:16px">Book An Appointment</a>

  <!-- Footer -->
  <svg class="abs" style="left:0;top:3640px" width="1200" height="545" viewBox="0 0 1200 545" aria-hidden="true">
    <path d="M0 170 Q600 -90 1200 170 L1200 545 L0 545 Z" fill="var(--coral)"/>
    <path d="M0 182 Q600 -70 1200 182 L1200 545 L0 545 Z" fill="var(--ink)"/>
  </svg>
  <div class="abs" style="left:0;top:3640px;width:270px;height:180px;background:radial-gradient(ellipse at 30% 70%,rgba(120,160,90,.55),rgba(120,160,90,0) 70%)" role="img" aria-label="Wild grass and small white flowers"></div>
  <div class="abs" style="left:950px;top:3640px;width:250px;height:180px;background:radial-gradient(ellipse at 70% 70%,rgba(120,160,90,.55),rgba(120,160,90,0) 70%)" role="img" aria-label="Wild grass and small white flowers"></div>

  <div class="brand" style="left:418px;top:3790px;color:var(--white)">
    <span class="mark" style="width:48px;height:48px"></span>
    <span class="name" style="font-size:34px">Bright Reed<br>Acupuncture Studio</span>
  </div>

  <nav class="footer-nav">
    <a style="left:271px">Home</a>
    <a style="left:398px">About Us</a>
    <a style="left:533px">Services</a>
    <a style="left:665px">Schedule</a>
    <a style="left:783px">FAQ</a>
    <a style="left:908px">Contact Us</a>
  </nav>

  <span class="social" style="left:476px" aria-label="Social link"></span>
  <span class="social" style="left:528px" aria-label="Social link"></span>
  <span class="social" style="left:578px" aria-label="Social link"></span>
  <span class="social" style="left:630px" aria-label="Social link"></span>
  <span class="social" style="left:681px" aria-label="Social link"></span>

  <p class="copyright">Copyright 2025.Company Name. All Rights Reserved</p>
</div>
</body>
</html>
```